Photography Price List DL flyer

In need of a double sided DL flyer to list prices for a photography business that is in the real estate industry. Will need to include logo and be themed to match. Price details and contact information are in the pdf attached.

Below are links to the logo and photos that can be used on the flyer.

Logo
https://www.filquarry.net/s/tmewqoral7bnzx/LogoFiles.zip?dl=0

Photos
https://www.filquarry.net/s/p3vhnkelo81rtw/Website_Images.zip?dl=0

Sorry people the photo examples I put the wrong link. I have fixed it in the brief but the proper link is: https://www.filquarry.net/s/p3vhnkelo81rtw/Website_Images.zip?dl=0

Also dimensions of a DL are 210mm x 99mm + 3m bleed. Thanks

Target Market(s)

Real estate agents

Industry/Entity Type

Business

Requirements
Must have
• Price lists and contact information

```html
<!DOCTYPE html>
<html lang="en">
<head>
<meta charset="utf-8">
<title>Brightnest Photos – DL Price Flyer</title>
<link rel="stylesheet" href="https://fonts.googleapis.com/css2?family=Arimo:wght@400;700&family=Bree+Serif&family=Oswald:wght@400;600&family=Raleway:wght@300&display=swap">
<style>
  :root{
    --pink:#ee6a70;
    --pink-dark:#d9555c;
    --green:#a8d47a;
    --green-dark:#8cbf5c;
    --ink:#333333;
    --paper:#fdf6f5;
    --stage:#ececec;
  }
  *{margin:0;padding:0;box-sizing:border-box}
  html,body{width:1200px;height:3038px;overflow:hidden;background:var(--stage)}
  .canvas{position:relative;width:1200px;height:3038px}
  .flyer-side{position:absolute;top:919px;width:566px;height:1200px;background:var(--paper);overflow:hidden;box-shadow:0 6px 18px rgba(0,0,0,.25)}
  .front{left:26px}
  .back{left:608px}

  /* front */
  .header-photo{position:absolute;left:0;top:0;width:566px;height:198px;background:linear-gradient(180deg,#4a4548,#242225)}
  .brand{position:absolute;left:28px;top:70px;display:flex;align-items:center;gap:16px;white-space:nowrap}
  .brand-name{font-family:"Raleway",sans-serif;font-weight:300;font-size:34px;letter-spacing:3px;color:var(--pink);text-transform:uppercase}
  .brand-dot{flex:0 0 56px;width:56px;height:56px;border-radius:50%;background:var(--pink)}
  .gallery{position:absolute;left:0;top:198px;width:566px;height:732px}
  .note{position:absolute;font-family:"Bree Serif",serif;color:var(--pink);font-size:28px;line-height:1.05;text-align:center}
  .note-team{left:345px;top:36px;width:210px}
  .note-work{left:40px;top:600px;width:220px}
  .photo-circle{position:absolute;width:194px;height:194px;border-radius:50%;border:5px solid #fff}
  .contact{position:absolute;left:0;top:930px;width:566px}
  .contact-row{height:55px;display:flex;align-items:center;justify-content:center;color:#fff;font-family:"Arimo",sans-serif;font-size:32px;white-space:nowrap}
  .contact-row.pink{background:var(--pink)}
  .contact-row.green{background:var(--green)}
  .contact-row.small{font-size:27px}
  .contact-title{font-family:"Oswald",sans-serif;font-weight:600;font-size:42px;letter-spacing:1px}
  .footer-photo{position:absolute;left:0;top:1150px;width:566px;height:50px;background:linear-gradient(90deg,#3a3538,#5b5356)}

  /* back */
  .prices-tab{position:absolute;left:56px;top:0;width:400px;height:92px;background:var(--green);border:3px solid var(--green-dark);border-top:none;border-radius:0 0 30px 30px;display:flex;align-items:center;justify-content:center;font-family:"Raleway",sans-serif;font-weight:300;font-size:52px;letter-spacing:22px;color:var(--pink)}
  .price-row{position:absolute;left:20px;width:450px;height:118px}
  .price-pill{position:absolute;left:130px;top:30px;width:272px;height:58px;background:var(--green);border-radius:0 14px 14px 0;display:flex;align-items:center;padding-left:44px;font-family:"Arimo",sans-serif;font-size:31px;color:var(--ink);white-space:nowrap}
  .price-badge{position:absolute;left:40px;top:0;width:118px;height:118px;border-radius:50%;background:var(--pink);border:6px solid var(--green);box-shadow:0 0 0 4px #fff inset;display:flex;align-items:center;justify-content:center;font-family:"Arimo",sans-serif;font-size:38px;color:#fff}
  .chevrons{position:absolute;left:0;top:0}
  .vertical-label{position:absolute;font-family:"Bree Serif",serif;color:var(--pink);transform:rotate(90deg);transform-origin:center;white-space:nowrap;text-align:center;font-size:52px;height:64px;line-height:64px}
  .label-photo{left:345px;top:260px;width:360px}
  .label-video{left:435px;top:838px;width:180px}
  .rule{position:absolute;left:40px;width:420px;height:2px;background:var(--ink)}
  .extras{position:absolute;left:0;top:540px;width:566px;height:110px}
  .extra-name{position:absolute;top:34px;font-family:"Bree Serif",serif;color:var(--pink);white-space:nowrap}
  .extra-note{position:absolute;left:18px;top:72px;font-family:"Arimo",sans-serif;font-size:10px;color:var(--ink);white-space:nowrap}
  .extra-badge{position:absolute;top:12px;width:84px;height:84px;border-radius:50%;background:var(--pink);border:4px solid var(--green);display:flex;align-items:center;justify-content:center;font-family:"Arimo",sans-serif;font-size:26px;color:#fff}
  .call-title{position:absolute;left:130px;top:1048px;font-family:"Oswald",sans-serif;font-weight:600;font-size:44px;color:var(--pink);letter-spacing:1px}
  .call-bar{position:absolute;left:40px;top:1113px;width:490px;height:82px;background:var(--pink);border-radius:22px 22px 0 0;display:flex;align-items:center;padding-left:26px;gap:14px;font-family:"Oswald",sans-serif;font-weight:600;font-size:54px;color:#fff;white-space:nowrap}
</style>
</head>
<body>
<main class="canvas">

  <section class="flyer-side front">
    <div class="header-photo" role="img" aria-label="Dim interior photograph of a living room behind the logo"></div>
    <div class="brand">
      <span class="brand-name">Brightnest Photos</span>
      <span class="brand-dot"></span>
    </div>

    <div class="gallery">
      <svg width="566" height="732" viewBox="0 0 566 732">
        <g fill="var(--pink)">
          <polygon points="33,198 95,90 220,90 283,198 220,306 95,306"/>
          <polygon points="287,302 349,194 474,194 537,302 474,410 349,410"/>
          <polygon points="33,426 95,318 220,318 283,426 220,534 95,534"/>
          <polygon points="287,562 349,454 474,454 537,562 474,670 349,670"/>
        </g>
        <g fill="none" stroke="var(--pink)" stroke-width="3" stroke-linecap="round">
          <path d="M470 122 Q520 150 506 196"/><path d="M494 184 L506 200 L516 186"/>
          <path d="M340 60 Q290 40 254 86"/><path d="M254 70 L252 90 L270 90"/>
          <path d="M60 590 Q20 540 50 500"/><path d="M36 506 L52 496 L58 514"/>
          <path d="M250 690 Q290 700 310 680"/><path d="M294 676 L312 678 L308 696"/>
        </g>
      </svg>
      <div class="photo-circle" role="img" aria-label="Portrait of a male photographer" style="left:61px;top:101px;background:linear-gradient(160deg,#8fa7c2,#3f5673)"></div>
      <div class="photo-circle" role="img" aria-label="Portrait of a female photographer" style="left:315px;top:205px;background:linear-gradient(160deg,#b99b86,#5b4638)"></div>
      <div class="photo-circle" role="img" aria-label="Photograph of a two-storey house exterior" style="left:61px;top:329px;background:linear-gradient(180deg,#c9dcea,#d8c7a8 55%,#6f9a4e)"></div>
      <div class="photo-circle" role="img" aria-label="Photograph of a modern interior with indoor plants" style="left:315px;top:465px;background:linear-gradient(160deg,#d9d2c8,#5e6b4e)"></div>
      <p class="note note-team">Our talented photographers</p>
      <p class="note note-work">some of their stunning photographs</p>
    </div>

    <div class="contact">
      <div class="contact-row pink"><span class="contact-title">CONTACT DETAILS</span></div>
      <div class="contact-row green">mobile: 0400 555 123</div>
      <div class="contact-row pink">web: brightnestphotos.com.au</div>
      <div class="contact-row green small">email: info@brightnestphotos.com.au</div>
    </div>
    <div class="footer-photo" role="img" aria-label="Strip of interior photograph"></div>
  </section>

  <section class="flyer-side back">
    <div class="prices-tab">PRICES</div>

    <div class="price-row" style="top:136px">
      <svg class="chevrons" width="450" height="118"><g fill="none" stroke="var(--green)" stroke-width="8"><path d="M30 42 L14 59 L30 76"/><path d="M416 42 L432 59 L416 76"/></g></svg>
      <div class="price-pill">10 images</div><div class="price-badge">$149</div>
    </div>
    <div class="price-row" style="top:246px">
      <svg class="chevrons" width="450" height="118"><g fill="none" stroke="var(--green)" stroke-width="8"><path d="M30 42 L14 59 L30 76"/><path d="M416 42 L432 59 L416 76"/></g></svg>
      <div class="price-pill">12-15 images</div><div class="price-badge">$179</div>
    </div>
    <div class="price-row" style="top:356px">
      <svg class="chevrons" width="450" height="118"><g fill="none" stroke="var(--green)" stroke-width="8"><path d="M30 42 L14 59 L30 76"/><path d="M416 42 L432 59 L416 76"/></g></svg>
      <div class="price-pill">20+ images</div><div class="price-badge">$229</div>
    </div>
    <div class="vertical-label label-photo">Photography</div>

    <div class="rule" style="top:516px"></div>

    <div class="extras">
      <span class="extra-name" style="left:18px;font-size:30px">Twilight</span>
      <span class="extra-note">(Add $100 to imagepackage)</span>
      <div class="extra-badge" style="left:176px">$100</div>
      <span class="extra-name" style="left:290px;font-size:25px;top:38px">Floorplans</span>
      <div class="extra-badge" style="left:446px">$49</div>
      <svg width="566" height="110" style="position:absolute;left:0;top:0"><g fill="none" stroke="var(--green)" stroke-width="5"><path d="M208 10 L218 0 L228 10"/><path d="M208 100 L218 110 L228 100"/><path d="M478 10 L488 0 L498 10"/><path d="M478 100 L488 110 L498 100"/><path d="M170 46 L162 54 L170 62"/><path d="M268 46 L276 54 L268 62"/><path d="M440 46 L432 54 L440 62"/><path d="M536 46 L544 54 L536 62"/></g></svg>
    </div>

    <div class="rule" style="top:670px"></div>

    <div class="price-row" style="top:698px">
      <svg class="chevrons" width="450" height="118"><g fill="none" stroke="var(--green)" stroke-width="8"><path d="M30 42 L14 59 L30 76"/><path d="M416 42 L432 59 L416 76"/></g></svg>
      <div class="price-pill">30 seconds</div><div class="price-badge">$150</div>
    </div>
    <div class="price-row" style="top:808px">
      <svg class="chevrons" width="450" height="118"><g fill="none" stroke="var(--green)" stroke-width="8"><path d="M30 42 L14 59 L30 76"/><path d="M416 42 L432 59 L416 76"/></g></svg>
      <div class="price-pill">60 seconds</div><div class="price-badge">$200</div>
    </div>
    <div class="price-row" style="top:918px">
      <svg class="chevrons" width="450" height="118"><g fill="none" stroke="var(--green)" stroke-width="8"><path d="M30 42 L14 59 L30 76"/><path d="M416 42 L432 59 L416 76"/></g></svg>
      <div class="price-pill">2 minutes</div><div class="price-badge">$300</div>
    </div>
    <div class="vertical-label label-video">Video</div>

    <svg width="120" height="80" style="position:absolute;left:30px;top:1046px"><g fill="none" stroke="var(--pink)" stroke-width="4" stroke-linecap="round"><path d="M92 30 Q40 20 30 62"/><path d="M18 50 L30 66 L42 52"/></g></svg>
    <div class="call-title">CALL US NOW!</div>
    <div class="call-bar">
      <span>0400 555 123</span>
      <svg width="40" height="62" viewBox="0 0 40 62"><rect x="3" y="3" width="34" height="56" rx="6" fill="none" stroke="#fff" stroke-width="5"/><circle cx="20" cy="50" r="3" fill="#fff"/></svg>
    </div>
  </section>

</main>
</body>
</html>
```